R. T. HOLLOWAY, INC. is a US based Investment firm looking for a five-page website design.

Currently, their temporary site is located at: rtholloway.com and they would like to maintain the site design as much as possible.

R. T. HOLLOWAY, INC. sister companies are: Crestvale Lodge Investments (c-lodge.com) Benwick Petroleum (benwick-petroleum.com) and RTHF (rth-foundation.org/en)

Attached is a .ZIP file with designs and assets we think will be useful for your proposal… Content for the site is attached on: rtholloway website content.docx Current temp website design is attached as: Coming Soon Website.zip .EPS Logo files attached as: rtholloway logos.zip Sample business card attached as: R T Holloway Business cards.eps Other assets, such as Fonts and background images attached as: Assets.zip

Target Market(s)

Investors

Industry/Entity Type

Investments

Number of Pages Required

5+ page

Requirements
Must have
• Contact Page with a form.

```html
<!DOCTYPE html>
<html lang="en">
<head>
<meta charset="utf-8">
<title>R. T. Holloway, Inc. — Investments</title>
<link href="https://fonts.googleapis.com/css2?family=Domine:wght@400;500&family=Cinzel:wght@400&family=Nunito+Sans:wght@400;600;700;800&display=swap" rel="stylesheet">
<style>
:root{
  --backdrop:#f4f4f4;
  --page:#ffffff;
  --navy:#161c27;
  --gold:#b19459;
  --blue:#1f4d7f;
  --ink:#222;
  --text:#4a4a4a;
  --muted:#cfd3da;
}
*{box-sizing:border-box;margin:0;padding:0}
html,body{width:1200px;height:3000px;overflow:hidden;background:var(--backdrop)}
body{font-family:"Nunito Sans",sans-serif;color:var(--text);position:relative}
.page{position:absolute;left:162px;top:48px;width:869px;height:2929px;background:var(--page);box-shadow:0 0 40px rgba(0,0,0,.08);overflow:hidden}
.abs{position:absolute}
.serif{font-family:"Domine",serif;color:var(--ink)}
.fill{position:absolute}

/* header */
.brand{left:49px;top:8px;text-align:center;width:76px}
.brand-dot{width:30px;height:30px;border:1.5px solid var(--gold);border-radius:50%;margin:0 auto 3px}
.brand-name{font-family:"Domine",serif;font-size:9.5px;color:#333;letter-spacing:.3px;white-space:nowrap}
.nav{top:20px;font-size:11px;color:#222}
.nav-divider{left:740px;top:18px;width:1px;height:18px;background:#bbb}
.round-btn{width:20px;height:20px;border-radius:50%;display:flex;align-items:center;justify-content:center}
.round-btn svg{width:8px;height:8px}

/* hero */
.hero{left:0;top:59px;width:869px;height:437px;background:linear-gradient(100deg,#3d3f44 0%,#2c3038 45%,#4e5258 70%,#2a2b2e 100%)}
.hero-title{left:49px;color:#fff;font-family:"Domine",serif;white-space:nowrap}
.hero-rule{height:2px;background:#fff;top:274px}
.hero-sub{left:49px;top:290px;color:#fff;font-size:13px;line-height:18px}
.hero-btn{left:48px;top:347px;width:114px;height:31px;border:1.5px solid #fff;color:#fff;font-size:11px;display:flex;align-items:center;padding-left:7px;gap:8px}
.hero-btn i{width:16px;height:16px;border:1px solid var(--gold);border-radius:50%}

/* about */
.section-h{font-size:26px}
.about-lead{left:49px;top:583px;width:450px;font-size:11px;line-height:15px;color:#444}
.about-rail{left:83px;top:652px;width:1px;height:280px;background:#888}
.about-label{left:71px;font-family:"Domine",serif;font-size:10.5px;color:var(--blue)}
.about-copy{left:97px;width:340px;font-size:9.5px;line-height:13px;color:#444}
.values{left:97px;top:856px;font-size:9.5px;line-height:13.3px;list-style:none;color:#444}
.values li::before{content:"• "}
.photo-frame{border:2px solid #fff}

/* investment */
.invest{left:0;top:1013px;width:869px;height:414px;background:var(--navy)}
.invest-h{left:0;width:869px;top:1050px;text-align:center;color:#fff;font-size:24px;font-family:"Domine",serif}
.ring{left:367px;top:1118px;width:134px;height:134px;border:5px solid var(--gold);border-radius:50%}
.sector-dot{width:48px;height:48px;border-radius:50%}
.sector{color:#fff}
.sector h3{font-family:"Cinzel",serif;font-weight:400;font-size:12px;letter-spacing:.4px}
.sector h4{font-size:7.5px;font-weight:400;margin-top:4px}
.sector p{font-size:7.5px;line-height:13px;margin-top:3px;color:#dfe2e7}

/* social */
.social-copy{left:468px;width:320px;font-size:10px;line-height:13px;color:#444}
.link-row{display:flex;align-items:center;gap:8px;font-size:10.5px;font-weight:700;color:#222}

/* case */
.case{left:0;top:1864px;width:869px;height:265px;background:linear-gradient(110deg,#5b5e63 0%,#3b3e43 45%,#2a2c30 100%)}
.case-h{left:0;width:869px;top:1910px;text-align:center;color:#fff;font-size:25px}
.case-p{left:138px;top:1962px;width:592px;text-align:center;color:#fff;font-size:11.5px;line-height:15px}

/* news */
.news-h{left:0;width:869px;top:2183px;text-align:center;font-size:24px}
.news-lead{left:190px;top:2232px;width:490px;text-align:center;font-size:10.5px;line-height:13px;color:#444}
.card-img{top:2297px;width:234px;height:172px}
.card-band{top:2442px;width:234px;height:27px;background:rgba(31,77,127,.9);color:#fff;font-size:9.5px;font-weight:700;padding:8px 0 0 10px}
.card-copy{top:2487px;width:222px;font-size:9.8px;line-height:14px;color:#444}
.card-more{top:2566px;font-size:9.5px;font-weight:700;color:var(--blue);text-decoration:underline}

/* footer */
.footer{left:0;top:2704px;width:869px;height:225px;background:var(--navy);color:#fff}
.foot-h{font-size:16px;font-weight:800;color:#fff}
.foot-links{list-style:none;font-size:8.5px;line-height:14.5px;color:#e6e8ec}
.foot-small{font-size:8.5px;color:#e6e8ec}
.social-dot{width:14px;height:14px;border:1.5px solid #fff;border-radius:50%}
</style>
</head>
<body>
<main class="page">

  <!-- header -->
  <header>
    <div class="abs brand"><div class="brand-dot"></div><div class="brand-name">R. T. HOLLOWAY</div></div>
    <nav>
      <span class="abs nav" style="left:356px">Home</span>
      <span class="abs nav" style="left:423px">About Us</span>
      <span class="abs nav" style="left:514px">Sector Areas</span>
      <span class="abs nav" style="left:618px">Social Responsibility</span>
      <span class="abs nav-divider"></span>
      <span class="abs nav" style="left:752px">Contact</span>
      <span class="abs round-btn" style="left:801px;top:17px;background:#111"><svg viewBox="0 0 8 8"><path d="M3 1l3 3-3 3" stroke="#fff" stroke-width="1.3" fill="none"/></svg></span>
    </nav>
  </header>

  <!-- hero -->
  <section>
    <div class="fill hero" role="img" aria-label="Two colleagues in a meeting with a financial chart overlay"></div>
    <div class="abs hero-title" style="top:185px;font-size:28px">GIVING FUTURE</div>
    <div class="abs hero-title" style="top:223px;font-size:36px">TO YOUR COMPANY</div>
    <div class="abs hero-rule" style="left:49px;width:100px"></div>
    <div class="abs hero-rule" style="left:170px;width:46px"></div>
    <p class="abs hero-sub">helping financial advisors to navigate<br>their journey to independence</p>
    <div class="abs hero-btn">LEARN MORE <i></i></div>
  </section>

  <!-- about -->
  <section>
    <h2 class="abs serif section-h" style="left:49px;top:535px;font-weight:400">About Us</h2>
    <p class="abs about-lead">Based In Houston, Texas, R. T. Holloway, Inc. Is An Investment Company, Founded In 2010, With The Purpose To Foster Endeavors For Socioeconomic Development, And Create Platforms For Harnessing The Potential Of World Resources</p>
    <div class="abs about-rail"></div>
    <div class="abs about-label" style="top:634px">Mission</div>
    <p class="abs about-copy" style="top:651px">Build a legacy for future generations through a differentiated selection and the development of, safe and high return investment opportunities for our customers, partners, and shareholders, generating a positive impact on the communities it serves.</p>
    <div class="abs about-label" style="top:703px">Vision</div>
    <p class="abs about-copy" style="top:730px;width:350px">R. T. Holloway, inc. is the main private investment company working towards the diversification and consolidation of national and regional economy</p>
    <div class="abs about-label" style="top:762px">Leadership</div>
    <p class="abs about-copy" style="top:786px;width:350px">R. T. Holloway, inc. is headed by robert t. holloway, lorem ipsum dolor sit amet, consectetur adipiscing elit. curabitur non quam ultricies, facilisis quam a, efficitur dolor morbi eget neque placerat eros aliquam commodo.</p>
    <div class="abs about-label" style="top:830px">Values</div>
    <ul class="abs values">
      <li>Integrity</li><li>Excellence</li><li>Responsibility</li><li>Transparency</li><li>Innovation</li><li>Organization</li>
    </ul>
    <div class="fill" style="left:613px;top:581px;width:207px;height:187px;background:linear-gradient(135deg,#b98d6a,#e9e3dc 60%,#c9ccd2)" role="img" aria-label="Hand placing a heart marker beside a laptop"></div>
    <div class="fill photo-frame" style="left:528px;top:700px;width:201px;height:172px;background:linear-gradient(135deg,#2f4a6a,#d9dde3 55%,#394a5e)" role="img" aria-label="Presenter pointing at charts on a screen"></div>
    <div class="fill photo-frame" style="left:620px;top:797px;width:193px;height:171px;background:linear-gradient(135deg,#e7e8ea,#b9bec6 50%,#2f3d52)" role="img" aria-label="Analyst at a desk with monitors and a calculator"></div>
  </section>

  <!-- investment areas -->
  <section>
    <div class="fill invest"></div>
    <h2 class="abs invest-h" style="font-weight:400">INVESTMENT AREAS</h2>
    <div class="abs ring"></div>
    <div class="abs sector-dot" style="left:286px;top:1106px;background:linear-gradient(#9db4cc,#6a7358)" role="img" aria-label="House"></div>
    <div class="abs sector-dot" style="left:528px;top:1124px;background:linear-gradient(#3c6fa8,#e6a24c)" role="img" aria-label="Solar panels at sunset"></div>
    <div class="abs sector-dot" style="left:298px;top:1226px;background:linear-gradient(#cfd6de,#7d8a98)" role="img" aria-label="Finance office"></div>
    <div class="abs sector-dot" style="left:504px;top:1226px;background:linear-gradient(#8fb1d4,#c98a3a)" role="img" aria-label="Mining truck"></div>
    <div class="abs sector-dot" style="left:411px;top:1273px;background:linear-gradient(#dde2e8,#6f7074)" role="img" aria-label="Industrial plant"></div>

    <div class="abs sector" style="left:105px;top:1110px;width:170px">
      <h3>Real Estate</h3><h4>PATIENTS ARE OUR "RAISON D'ÊTRE</h4>
      <p>By focussing on the needs and requirements of our patients, partners and customers, we fulfil our mission and generate additional values for all.</p>
    </div>
    <div class="abs sector" style="left:114px;top:1219px;width:160px">
      <h3>Finance</h3><h4>ONE MIND, ONE HEART</h4>
      <p>by working together we draw on our strengths. we work all for one and one for all to succeed.</p>
    </div>
    <div class="abs sector" style="left:592px;top:1119px;width:140px">
      <h3>Energy</h3><h4>PASSION TO LEAD</h4>
      <p>By setting clear objectives we create new value.</p>
    </div>
    <div class="abs sector" style="left:578px;top:1223px;width:160px">
      <h3>Mining</h3><h4>ALWAYS PROFESSIONAL</h4>
      <p>Patients are our "raison d'être"-By focussing on the needs and requirements of our patients</p>
    </div>
    <div class="abs sector" style="left:360px;top:1327px;width:150px;text-align:center">
      <h3>Industry</h3><h4>DARE TO SHARE</h4>
      <p>By working together we draw on our strengths. We work all for one and one for all to succeed.</p>
    </div>
  </section>

  <!-- social responsibility -->
  <section>
    <div class="fill" style="left:89px;top:1487px;width:175px;height:156px;background:linear-gradient(135deg,#5a6a5a,#b99a83 50%,#3d4a55)" role="img" aria-label="Hands together holding a seedling"></div>
    <div class="fill" style="left:187px;top:1552px;width:188px;height:169px;border:2px solid #fff;background:linear-gradient(135deg,#d6d7d9,#bfc1c4)" role="img" aria-label="Raised hands holding a globe, a light bulb and a wind turbine"></div>
    <div class="fill" style="left:96px;top:1673px;width:157px;height:140px;background:linear-gradient(135deg,#d7c3b0,#a7806a 55%,#e2d8cf)" role="img" aria-label="Hands stacked together"></div>
    <h2 class="abs serif section-h" style="left:496px;top:1522px;font-weight:500">Social Responsibility</h2>
    <p class="abs social-copy" style="left:496px;top:1572px;width:306px">Since The Commencement Of Our Activity, R. T. Holloway, Inc. Contributes To Change The Quality Of Life Of Children And Seniors Across The World, Providing Them With Support For Primary Education And Basic Medical Aid, Which We Believe To Be The Right Of Every Human Being</p>
    <p class="abs social-copy" style="left:494px;top:1651px;width:315px;font-size:11px;line-height:15px">Proportionally To Our Growth, R. T. Holloway, Inc. Aims To Extend Our Contributions To Other Communities In Africa And The Rest Of The World, With More Donations To Charities And Other Non-Profit Organizations Via The Robert T. Holloway Foundation</p>
    <div class="abs link-row" style="left:499px;top:1737px">Learn More <span class="round-btn" style="background:var(--blue)"><svg viewBox="0 0 8 8"><path d="M3 1l3 3-3 3" stroke="#fff" stroke-width="1.3" fill="none"/></svg></span></div>
  </section>

  <!-- case study -->
  <section>
    <div class="fill case" role="img" aria-label="Business handshake"></div>
    <h2 class="abs serif case-h" style="color:#fff;font-weight:400">Case Study</h2>
    <p class="abs case-p">Lorem Ipsum Dolor Sit Amet, Consectetur Adipiscing Elit. At Suspendisse Tortor Bibendum Odio Sollicitudin Eleifend Nisl, Consectetur. Lobortis Dictum Mauris Bibendum Sollicitudin Libero Feugiat. Sem Rutrum Felis Sagittis, Quam Pellentesque Magna Pellentesque. Tortor Ultrices Vel Eu Nec Nec Sed Commodo. Tristique Viverra Metus Pellentesque Integer.Lorem Ipsum Dolor Sit Amet, Consectetur Adipiscing Elit</p>
    <div class="abs link-row" style="left:392px;top:2049px;color:#fff">Learn More <span class="round-btn" style="background:#fff"><svg viewBox="0 0 8 8"><path d="M3 1l3 3-3 3" stroke="#222" stroke-width="1.3" fill="none"/></svg></span></div>
  </section>

  <!-- news -->
  <section>
    <h2 class="abs serif news-h" style="font-weight:400">News/Articals</h2>
    <p class="abs news-lead">Lorem ipsum dolor sit amet, consectetur adipiscing elit. Nibh odio aliquet vel id quis orci, diam mi, in. Eleifend quam id gravida urna, a sed. Blandit tellus amet felis sit congue.</p>

    <div class="fill card-img" style="left:55px;background:linear-gradient(135deg,#1b2330,#33435a 60%,#1a2029)" role="img" aria-label="Stock market chart on a screen"></div>
    <div class="abs card-band" style="left:55px">Lorem ipsum dolor sit amet,</div>
    <p class="abs card-copy" style="left:64px">Lorem ipsum dolor sit amet, consectetur adipiscing elit. Nibh odio aliquet vel id quis orci, diam mi, in. Eleifend quam id gravida urna, a sed. Blandit tellus amet felis sit congue.</p>
    <span class="abs card-more" style="left:237px">Learn More</span>

    <div class="fill card-img" style="left:318px;background:linear-gradient(135deg,#d9dde2,#f2f3f5 50%,#7e9bc0)" role="img" aria-label="Hands with a pen over printed charts"></div>
    <div class="abs card-band" style="left:318px">Lorem ipsum dolor sit amet,</div>
    <p class="abs card-copy" style="left:326px">Lorem ipsum dolor sit amet, consectetur adipiscing elit. Nibh odio aliquet vel id quis orci, diam mi, in. Eleifend quam id gravida urna, a sed. Blandit tellus amet felis sit congue.</p>
    <span class="abs card-more" style="left:501px">Learn More</span>

    <div class="fill card-img" style="left:580px;background:linear-gradient(135deg,#e8cfcf,#f4eeee 50%,#6b3a35)" role="img" aria-label="Person writing notes beside a calculator"></div>
    <div class="abs card-band" style="left:580px">Lorem ipsum dolor sit amet,</div>
    <p class="abs card-copy" style="left:588px">Lorem ipsum dolor sit amet, consectetur adipiscing elit. Nibh odio aliquet vel id quis orci, diam mi, in. Eleifend quam id gravida urna, a sed. Blandit tellus amet felis sit congue.</p>
    <span class="abs card-more" style="left:763px">Learn More</span>

    <div class="abs link-row" style="left:394px;top:2624px">View More <span class="round-btn" style="background:var(--blue)"><svg viewBox="0 0 8 8"><path d="M3 1l3 3-3 3" stroke="#fff" stroke-width="1.3" fill="none"/></svg></span></div>
  </section>

  <!-- footer -->
  <footer>
    <div class="fill footer"></div>
    <div class="abs" style="left:122px;top:2744px;width:28px;height:28px;border:1.5px solid var(--gold);border-radius:50%"></div>
    <div class="abs" style="left:61px;top:2779px;width:172px;text-align:center;font-family:'Domine',serif;font-size:10px;color:#fff">R. T. HOLLOWAY</div>
    <p class="abs foot-small" style="left:58px;top:2801px;width:178px;text-align:center;line-height:12px">Based In Houston, Texas, R. T. Holloway, Inc. Is An Investment Company, Founded In 2010, With The Purpose To Foster Endeavors For Socioeconomic Development, And Create Platforms For Harnessing The Potential Of World Resources</p>

    <div class="abs foot-h" style="left:329px;top:2760px">Quick Links</div>
    <ul class="abs foot-links" style="left:329px;top:2792px">
      <li>Home</li><li>About Us</li><li>Investment Areas</li><li>Social Responsibility</li><li>Contact Us</li>
    </ul>

    <div class="abs foot-h" style="left:500px;top:2760px">Contact us</div>
    <svg class="abs" style="left:502px;top:2796px" width="12" height="12" viewBox="0 0 24 24"><path d="M6.6 10.8a15 15 0 006.6 6.6l2.2-2.2a1 1 0 011-.25 11.4 11.4 0 003.6.57 1 1 0 011 1V20a1 1 0 01-1 1A17 17 0 013 4a1 1 0 011-1h3.5a1 1 0 011 1c0 1.25.2 2.45.57 3.57a1 1 0 01-.25 1z" fill="#fff"/></svg>
    <span class="abs foot-small" style="left:524px;top:2797px">1300 555 019</span>
    <svg class="abs" style="left:502px;top:2828px" width="13" height="10" viewBox="0 0 13 10"><rect x=".6" y=".6" width="11.8" height="8.8" fill="none" stroke="#fff"/><path d="M.6.6l5.9 5 5.9-5" fill="none" stroke="#fff"/></svg>
    <span class="abs foot-small" style="left:524px;top:2827px">www.rtholloway.com.au</span>

    <div class="abs foot-h" style="left:683px;top:2760px">Follow us</div>
    <span class="abs social-dot" style="left:667px;top:2796px"></span>
    <span class="abs social-dot" style="left:699px;top:2796px"></span>
    <span class="abs social-dot" style="left:731px;top:2796px"></span>
    <span class="abs social-dot" style="left:763px;top:2796px"></span>

    <div class="abs" style="left:69px;top:2897px;width:738px;height:1px;background:#5a606b"></div>
    <div class="abs foot-small" style="left:0;width:869px;top:2907px;text-align:center">© copyright 2021 All Right R.T. Holloway</div>
  </footer>

</main>
</body>
</html>
```